Stationery Design Project

We need a stationery design for a new business consulting business based in New Zealand.
We have the logo and business cards designed and we're looking for letterhead, compliments slip and PowerPoint presentation format that aligns with our business cards.
Industry/Entity Type
Business
Requirements
Must have
- same colors and format as business cards

```html
<!DOCTYPE html>
<html lang="en">
<head>
<meta charset="utf-8">
<title>Wrenmoor Advisory – Presentation Template</title>
<link rel="stylesheet" href="https://fonts.googleapis.com/css2?family=Jost:wght@400;500;700&family=Arimo:wght@400&display=swap">
<style>
  :root {
    --backdrop: #4b4a47;
    --slide-light: #ffffff;
    --slide-edge: #c5c6c8;
    --brand-green: #8dc63f;
    --side-grey: #a3a4a6;
    --text-dark: #4f5053;
    --text-mid: #58595b;
    --text-soft: #8a8b8d;
    --faint-word: rgba(255, 255, 255, 0.5);
    --bar-red: #e8423a;
    --bar-blue: #4155b4;
    --bar-green: #2fae5a;
    --bar-yellow: #f2d62a;
  }
  html, body {
    margin: 0;
    padding: 0;
    width: 1200px;
    height: 849px;
    overflow: hidden;
  }
  body {
    background: var(--backdrop);
    position: relative;
    font-family: "Jost", "Century Gothic", sans-serif;
  }
  .slide {
    position: absolute;
    width: 560px;
    height: 419px;
    overflow: hidden;
    background: radial-gradient(ellipse 60% 60% at 50% 48%, var(--slide-light) 0%, #e9eaeb 45%, var(--slide-edge) 100%);
  }
  .slide--title { left: 65px; top: 24px; }
  .slide--content { left: 577px; top: 405px; width: 558px; height: 418px; }
  .accent-band {
    position: absolute;
    top: 0;
    right: 0;
    height: 18px;
    background: var(--brand-green);
  }
  .slide--title .accent-band { width: 313px; }
  .slide--content .accent-band { width: 252px; }
  .side-band {
    position: absolute;
    left: 0;
    bottom: 0;
    width: 18px;
    background: var(--side-grey);
  }
  .slide--title .side-band { height: 165px; }
  .slide--content .side-band { height: 210px; }

  .faint-word {
    position: absolute;
    left: 50px;
    top: 50px;
    margin: 0;
    font-size: 128px;
    font-weight: 700;
    line-height: 1;
    letter-spacing: -4px;
    color: var(--faint-word);
  }
  .brand-name {
    position: absolute;
    margin: 0;
    font-weight: 500;
    color: var(--brand-green);
    white-space: nowrap;
    line-height: 1;
  }
  .slide--title .brand-name {
    left: 115px;
    top: 116px;
    font-size: 44px;
    letter-spacing: -0.5px;
  }
  .slide--content .brand-name {
    right: 28px;
    bottom: 16px;
    font-size: 26px;
  }
  .presentation-title {
    position: absolute;
    left: 153px;
    top: 249px;
    margin: 0;
    font-size: 20px;
    font-weight: 700;
    line-height: 24px;
    letter-spacing: 0.6px;
    color: var(--brand-green);
  }
  .presentation-subtitle {
    position: absolute;
    left: 153px;
    top: 310px;
    margin: 0;
    font-size: 16px;
    font-weight: 400;
    line-height: 19px;
    letter-spacing: 0.4px;
    color: var(--text-mid);
  }

  .slide-heading {
    position: absolute;
    left: 43px;
    top: 20px;
    margin: 0;
    font-size: 18px;
    font-weight: 700;
    letter-spacing: 0.3px;
    color: var(--text-dark);
  }
  .slide-subheading {
    position: absolute;
    left: 43px;
    top: 42px;
    margin: 0;
    font-size: 14.5px;
    letter-spacing: 0.3px;
    color: var(--text-soft);
  }
  .bullet-list {
    position: absolute;
    left: 43px;
    top: 85px;
    width: 254px;
    margin: 0;
    padding: 0;
    list-style: none;
    font-family: "Arimo", "Helvetica", sans-serif;
    font-size: 15px;
    line-height: 20.3px;
    color: #1f1f1f;
  }
  .bullet-list li {
    position: relative;
    padding-left: 14px;
  }
  .bullet-list li::before {
    content: "";
    position: absolute;
    left: 1px;
    top: 8px;
    width: 4px;
    height: 4px;
    border-radius: 50%;
    background: var(--brand-green);
  }
  .bullet-list .sub-list {
    margin: 0;
    padding: 0;
    list-style: none;
  }
  .bullet-list .sub-list li { padding-left: 13px; }
  .bar-chart {
    position: absolute;
    left: 326px;
    top: 120px;
  }
</style>
</head>
<body>
  <section class="slide slide--title" aria-label="Title slide">
    <div class="accent-band"></div>
    <div class="side-band"></div>
    <p class="faint-word" aria-hidden="true">wren</p>
    <p class="brand-name">Wrenmoor Advisory</p>
    <h1 class="presentation-title">Insert The Title of Your<br>Presentation Here</h1>
    <p class="presentation-subtitle">Subtitle of the Presentation<br>or main author’s name here</p>
  </section>

  <section class="slide slide--content" aria-label="Content slide">
    <div class="accent-band"></div>
    <div class="side-band"></div>
    <h2 class="slide-heading">Sample Slide - Bullet Points</h2>
    <p class="slide-subheading">Placeholder for subtitle</p>
    <ul class="bullet-list">
      <li>The text demonstrates how your own text will look when you replace the placeholder with your own text.
        <ul class="sub-list">
          <li>The text demonstrates how your own text will look when you replace the placeholder with your own text.</li>
          <li>The text demonstrates how your own text will look when you replace the placeholder with your own text.</li>
        </ul>
      </li>
    </ul>
    <svg class="bar-chart" width="200" height="175" viewBox="0 0 200 175" role="img" aria-label="Bar chart with four bars">
      <rect x="2" y="50" width="52" height="120" rx="3" fill="var(--bar-red)"/>
      <rect x="48" y="0" width="54" height="160" rx="3" fill="var(--bar-blue)"/>
      <rect x="100" y="22" width="50" height="132" rx="3" fill="var(--bar-green)"/>
      <rect x="146" y="50" width="48" height="98" rx="3" fill="var(--bar-yellow)"/>
    </svg>
    <p class="brand-name">Wrenmoor Advisory</p>
  </section>
</body>
</html>
```